I need a business card for myself, being a proprietor of a funeral parlor based in Manila. I'd like the card to have either of the following:
White Font on Black Background
or
Black Font on White Background
No logo is needed however I will appreciate any efforts to show a symbol of eternal happiness, aptly designed with above mentioned colors in mind.
Company name, address and contact on the lower right corner.
Logo or symbol anywhere.
Quillstone Funeral Services
+639174826351
darvik4521@pelmora.com
corner of Brisco Avenue and Velhurst Street
Makati City, Philippines
Thank you.
Update: Please include a small dove in your design. You are free to choose where you would like it on the card.

```html
<!DOCTYPE html>
<html lang="en">
<head>
<meta charset="utf-8">
<title>Quillstone Funeral Services – Business Card</title>
<link rel="stylesheet" href="https://fonts.googleapis.com/css2?family=Open+Sans:wght@400;700&display=swap">
<style>
  :root {
    --backdrop: #1b1b1b;
    --card: #ffffff;
    --card-shade: #ececec;
    --ink: #1f1f1f;
    --ink-soft: #3a3a3a;
    --rule: #4a4a4a;
    --accent: #8cc63f;
  }
  * { margin: 0; padding: 0; box-sizing: border-box; }
  html, body {
    width: 1200px;
    height: 871px;
    overflow: hidden;
    background: var(--backdrop);
    font-family: "Open Sans", sans-serif;
  }
  .stage {
    position: relative;
    width: 1200px;
    height: 871px;
  }
  .business-card {
    position: absolute;
    left: 100px;
    top: 150px;
    width: 1000px;
    height: 571px;
    background: linear-gradient(135deg, var(--card) 55%, var(--card-shade) 100%);
    border-radius: 4px;
    box-shadow: 0 20px 50px rgba(0,0,0,0.6);
  }
  .brand {
    position: absolute;
    left: 200px;
    top: 120px;
    display: flex;
    align-items: center;
    gap: 22px;
  }
  .brand-mark {
    width: 64px;
    height: 64px;
    border-radius: 50%;
    background: var(--accent);
    flex: none;
  }
  .brand-name {
    font-size: 38px;
    font-weight: 700;
    color: var(--ink);
    letter-spacing: 0.5px;
  }
  .contact {
    position: absolute;
    left: 290px;
    top: 300px;
    list-style: none;
    color: var(--ink-soft);
    font-size: 21px;
    line-height: 1.3;
  }
  .contact-row {
    display: flex;
    align-items: flex-start;
    gap: 14px;
    padding: 4px 0 4px;
  }
  .contact-row.ruled {
    border-bottom: 1.5px solid var(--rule);
    width: 290px;
    margin-bottom: 6px;
  }
  .contact-icon {
    width: 20px;
    height: 20px;
    flex: none;
    margin-top: 4px;
    fill: var(--ink);
  }
</style>
</head>
<body>
<main class="stage">
  <section class="business-card">
    <div class="brand">
      <span class="brand-mark"></span>
      <span class="brand-name">Quillstone Funeral Services</span>
    </div>
    <ul class="contact">
      <li class="contact-row ruled">
        <svg class="contact-icon" viewBox="0 0 24 24" aria-hidden="true"><path d="M6.6 10.8a15.1 15.1 0 0 0 6.6 6.6l2.2-2.2a1 1 0 0 1 1-.25 11.4 11.4 0 0 0 3.6.57 1 1 0 0 1 1 1V20a1 1 0 0 1-1 1A17 17 0 0 1 3 4a1 1 0 0 1 1-1h3.5a1 1 0 0 1 1 1c0 1.25.2 2.45.57 3.57a1 1 0 0 1-.25 1z"/></svg>
        <span>(63)-9174826351</span>
      </li>
      <li class="contact-row ruled">
        <svg class="contact-icon" viewBox="0 0 24 24" aria-hidden="true"><path d="M2 5h20v14H2zM4 7v.5l8 5 8-5V7zm0 2.9V17h16V9.9l-8 5z"/></svg>
        <span>darvik4521@pelmora.com</span>
      </li>
      <li class="contact-row">
        <svg class="contact-icon" viewBox="0 0 24 24" aria-hidden="true"><path d="M12 2a7 7 0 0 0-7 7c0 5.2 7 13 7 13s7-7.8 7-13a7 7 0 0 0-7-7zm0 9.5A2.5 2.5 0 1 1 12 6.5a2.5 2.5 0 0 1 0 5z"/></svg>
        <span>corner of Brisco Avenue and Velhurst Street<br>Makati City, Philippines</span>
      </li>
    </ul>
  </section>
</main>
</body>
</html>
```